Willowmere Counseling (Endure - Mend - Flourish) - Double Sided Business Card

I would like a 2-sided business card. Front: Matte Black or Navy with Logo & Tagline. Back: Name, Address, Phone Number, Email, & Website (maybe would like to include a small map pin-pointing location); Prefer front to be a gold/silver foil (iridescent); Back prefer white or light colored background with lettering that is easy to read and simple

Target Market(s)

Individuals & Couples (13 y.o. - ALL Adults); High end clientele

Industry/Entity Type

Licensed Professional Counselor (Mental Health)

Contact Information for Business Card

Name: Willowmere Counseling; Tagline: Endure - Mend - Flourish; Address: 3870 N. Garrick Ave., Suite 214, Fort Worth, TX 76132; Phone: (214) 555-0187; Website: www.WillowmereCounseling.example

Font styles to use
Serif

Requirements
Must have
• Logo on Front (Large) prefer gold/silver foil on a matte dark color (i.e. black, navy, etc.); Back of Card: All other relevant information

```html
<!DOCTYPE html>
<html lang="en">
<head>
<meta charset="utf-8">
<title>Willowmere Counseling – Business Card</title>
<link rel="stylesheet" href="https://fonts.googleapis.com/css2?family=Cinzel:wght@400;600&family=Roboto:wght@400;500;700&display=swap">
<style>
  :root {
    --page: #e4e4e4;
    --card: #1e1e1e;
    --card-edge: #b39a45;
    --gold: #d4b65a;
    --gold-foil: linear-gradient(135deg, #b8983f 0%, #e8d48f 45%, #b08f3a 70%, #dcc27a 100%);
    --silver: #d9d9d9;
    --text-light: #e6e6e6;
  }
  * { box-sizing: border-box; margin: 0; padding: 0; }
  html, body { width: 1200px; height: 884px; overflow: hidden; background: var(--page); }
  .sheet {
    width: 1200px; height: 884px;
    display: flex; flex-direction: column; align-items: center; justify-content: center; gap: 44px;
  }
  .card {
    width: 640px; height: 366px;
    background: var(--card);
    border: 2px solid var(--card-edge);
    border-radius: 3px;
    box-shadow: 0 10px 24px rgba(0,0,0,.22);
    position: relative;
  }
  /* Front */
  .card--front { display: flex; align-items: center; justify-content: center; }
  .wordmark { display: flex; flex-direction: column; align-items: center; }
  .wordmark__row { display: flex; align-items: center; gap: 18px; }
  .wordmark__dot { width: 46px; height: 46px; border-radius: 50%; background: var(--gold-foil); }
  .wordmark__name {
    font-family: "Cinzel", serif; font-weight: 400; color: var(--gold);
    font-size: 50px; letter-spacing: 3px; line-height: 1;
  }
  .wordmark__sub {
    font-family: "Cinzel", serif; font-weight: 400; color: var(--gold);
    font-size: 22px; letter-spacing: 10px; margin-top: 10px;
  }
  .wordmark__rule { width: 100%; height: 2px; background: var(--gold); margin: 12px 0 10px; }
  .wordmark__tagline {
    font-family: "Cinzel", serif; color: var(--gold); font-size: 16px; letter-spacing: 2px;
  }
  /* Back */
  .card--back { display: flex; align-items: center; padding: 0 34px; }
  .back__brand { width: 260px; display: flex; flex-direction: column; align-items: center; }
  .back__brand .wordmark__dot { width: 26px; height: 26px; background: var(--gold); }
  .back__brand .wordmark__row { gap: 10px; }
  .back__brand .wordmark__name { font-size: 25px; letter-spacing: 1.5px; }
  .back__brand .wordmark__sub { font-size: 12px; letter-spacing: 6px; margin-top: 6px; color: var(--silver); }
  .back__brand .wordmark__rule { background: var(--silver); margin: 7px 0 6px; height: 1.5px; }
  .back__brand .wordmark__tagline { font-size: 9.5px; letter-spacing: 1px; }
  .divider {
    width: 1px; height: 230px; margin: 0 28px;
    background: linear-gradient(to bottom, transparent, #8a8a8a 50%, transparent);
  }
  .contact { font-family: "Roboto", sans-serif; color: var(--text-light); font-size: 14.5px; line-height: 1.45; }
  .contact__company { color: var(--gold); font-weight: 700; font-size: 17px; letter-spacing: .3px; }
  .contact__role { font-weight: 700; font-size: 15.5px; margin-bottom: 12px; }
  .contact__address { margin-bottom: 8px; }
  .contact__line { display: flex; align-items: center; gap: 9px; }
  .contact__line svg { width: 14px; height: 14px; flex: none; }
</style>
</head>
<body>
<main class="sheet">
  <section class="card card--front" aria-label="Card front">
    <div class="wordmark">
      <div class="wordmark__row">
        <span class="wordmark__dot"></span>
        <span class="wordmark__name">WILLOWMERE</span>
      </div>
      <span class="wordmark__sub">COUNSELING</span>
      <span class="wordmark__rule"></span>
      <span class="wordmark__tagline">ENDURE - MEND - FLOURISH</span>
    </div>
  </section>

  <section class="card card--back" aria-label="Card back">
    <div class="back__brand wordmark">
      <div class="wordmark__row">
        <span class="wordmark__dot"></span>
        <span class="wordmark__name">WILLOWMERE</span>
      </div>
      <span class="wordmark__sub">COUNSELING</span>
      <span class="wordmark__rule"></span>
      <span class="wordmark__tagline">ENDURE - MEND - FLOURISH</span>
    </div>
    <div class="divider"></div>
    <div class="contact">
      <div class="contact__company">WILLOWMERE COUNSELING</div>
      <div class="contact__role">Managing Director</div>
      <div class="contact__address">3870 N. Garrick Ave., Suite 214,<br>Fort Worth, TX 76132</div>
      <div class="contact__line">
        <svg viewBox="0 0 24 24" fill="#d4b65a" aria-hidden="true"><path d="M6.6 10.8a15 15 0 006.6 6.6l2.2-2.2a1 1 0 011-.25 11.4 11.4 0 003.6.57 1 1 0 011 1V20a1 1 0 01-1 1A17 17 0 013 4a1 1 0 011-1h3.5a1 1 0 011 1c0 1.25.2 2.45.57 3.57a1 1 0 01-.25 1z"/></svg>
        <span>(214) 555-0187</span>
      </div>
      <div class="contact__line">
        <svg viewBox="0 0 24 24" fill="#d4b65a" aria-hidden="true"><path d="M2 5h20v14H2z"/><path d="M2 5l10 8 10-8" fill="none" stroke="#1e1e1e" stroke-width="1.6"/></svg>
        <span>info@WillowmereCounseling.example</span>
      </div>
      <div class="contact__line">
        <svg viewBox="0 0 24 24" fill="none" stroke="#d4b65a" stroke-width="2" aria-hidden="true"><circle cx="12" cy="12" r="9"/><path d="M3 12h18M12 3c3 3.5 3 14.5 0 18M12 3c-3 3.5-3 14.5 0 18"/></svg>
        <span>www.WillowmereCounseling.example</span>
      </div>
    </div>
  </section>
</main>
</body>
</html>
```